Eye Catching Stylish Seminar Flyer

Design a Business Seminar Flyer that will be used for Print and Web distribution that is professional, eye catching in its color scheme and fonts.

have www.brightledgerday.com to register

Target Market(s)

Who is this for: business owners, marketplace professionals, homemakers.

Industry/Entity Type

Business Consultant

Font styles to use
Serif

Colors
abd037

Requirements
Must have
• Great colors, great Font
Nice to have
• Design a simple professional text based Logo for the Event that encapsulates For the flyer. Eye catching designs that provoke action in the reader of the flyer.
Should not have
• Cross designs stereotypical designs that are associated with religion. Rather they should be creative toward people that own businesses and work with colleagues in a daily office, school etc.

```html
<!DOCTYPE html>
<html lang="en">
<head>
<meta charset="utf-8">
<title>The Voice in the Market Place – Seminar Flyer</title>
<link rel="stylesheet" href="https://fonts.googleapis.com/css2?family=Archivo:wght@800&family=Marcellus&family=Marcellus+SC&family=Source+Sans+3:wght@400;600;700&display=swap">
<style>
  :root{
    --maroon:#7e1b2b;
    --rust:#c6482a;
    --gold:#e7c46a;
    --gold-deep:#b98a3a;
    --cream:#f6e7b8;
    --white:#ffffff;
  }
  html,body{margin:0;padding:0;overflow:hidden;background:#fff;}
  .flyer{position:relative;width:927px;height:1200px;overflow:hidden;font-family:"Source Sans 3",sans-serif;}
  .hero-photo{position:absolute;left:0;top:0;width:927px;height:668px;
    background:linear-gradient(100deg,#8a8f95 0%,#cfc7bf 22%,#efece6 45%,#f5f3ee 70%,#e4e0d6 100%);}
  .brand-badge{position:absolute;left:312px;top:36px;width:224px;height:224px;border-radius:50%;background:var(--white);
    display:flex;flex-direction:column;align-items:center;justify-content:center;box-shadow:0 2px 8px rgba(0,0,0,.15);}
  .brand-badge span{font-family:"Marcellus",serif;color:var(--maroon);font-size:27px;line-height:1.1;text-align:center;}
  .presenter{position:absolute;right:53px;top:204px;font-family:"Source Sans 3",sans-serif;font-weight:700;font-size:25px;color:var(--maroon);}
  .title-line{position:absolute;right:53px;font-family:"Archivo",sans-serif;font-weight:800;line-height:1;letter-spacing:-1px;
    background:linear-gradient(180deg,#fbe79a 0%,var(--gold) 45%,var(--gold-deep) 100%);-webkit-background-clip:text;background-clip:text;color:transparent;
    filter:drop-shadow(2px 3px 2px rgba(60,30,10,.55));white-space:nowrap;}
  .title-line small{font-size:.58em;}
  .l1{top:232px;font-size:92px;}
  .l2{top:327px;font-size:92px;}
  .l3{top:418px;font-size:52px;}
  .l4{top:472px;font-size:100px;}
  .l5{top:572px;font-size:100px;}
  .info-band{position:absolute;left:0;top:668px;width:927px;height:464px;background:var(--maroon);border-top:2px solid var(--gold-deep);}
  .tagline{position:absolute;left:0;width:927px;top:12px;margin:0;font-weight:400;text-align:center;font-family:"Marcellus SC",serif;font-size:50px;color:var(--gold);}
  .dates{position:absolute;left:68px;top:102px;width:386px;height:90px;background:var(--rust);border:2px solid var(--gold);box-sizing:border-box;
    padding:9px 0 0 28px;color:var(--white);}
  .dates p{margin:0;font-size:32px;line-height:35px;height:35px;white-space:nowrap;}
  .dates sup{font-size:18px;line-height:0;vertical-align:super;}
  .dates .time{font-size:20px;margin-left:8px;}
  .divider{position:absolute;left:482px;top:96px;width:2px;height:240px;background:var(--rust);}
  .featuring{position:absolute;left:505px;top:92px;font-family:"Source Sans 3",sans-serif;font-weight:700;font-size:60px;line-height:60px;color:var(--rust);letter-spacing:1px;}
  .speakers{position:absolute;left:507px;top:158px;margin:0;padding:0;list-style:none;color:var(--white);font-size:25px;line-height:34.8px;}
  .fee{position:absolute;left:96px;top:216px;width:212px;height:212px;border-radius:50%;background:radial-gradient(circle at 45% 40%,#d1552f,var(--rust) 70%);
    box-shadow:0 0 0 2px var(--gold-deep);text-align:center;font-family:"Archivo",sans-serif;font-weight:800;}
  .fee .label{display:block;margin-top:28px;font-size:48px;color:var(--gold);}
  .fee .amount{display:block;font-size:80px;line-height:80px;color:var(--cream);filter:drop-shadow(2px 3px 2px rgba(60,20,10,.6));}
  .includes{position:absolute;left:310px;top:368px;width:580px;margin:0;font-size:26px;line-height:30px;color:var(--gold);}
  .web-band{position:absolute;left:0;top:1132px;width:927px;height:68px;background:var(--rust);border-top:2px solid var(--gold);
    text-align:center;font-size:48px;line-height:66px;color:var(--gold);}
</style>
</head>
<body>
<main class="flyer">
  <div class="hero-photo" role="img" aria-label="Photo of smiling professionals meeting around an office table"></div>
  <div class="brand-badge"><span>LEDGERLIGHT<br>COLLECTIVE</span></div>
  <div class="presenter">LEDGERLIGHT COLLECTIVE presents</div>
  <div class="title-line l1"><small>THE </small>VOICE</div>
  <div class="title-line l2"><small>OF THE </small>LORD</div>
  <div class="title-line l3">IN THE</div>
  <div class="title-line l4">MARKET</div>
  <div class="title-line l5">PLACE</div>

  <section class="info-band">
    <h2 class="tagline">Moving from Intimacy to Impact</h2>
    <div class="dates">
      <p>MARCH 24<sup>th</sup><span class="time">6PM-9:20PM</span></p>
      <p>MARCH 25<sup>th</sup><span class="time">8:30AM-2:20PM</span></p>
    </div>
    <div class="divider"></div>
    <div class="featuring">FEATURING</div>
    <ul class="speakers">
      <li>Marcus Hale: Author/Podcaster</li>
      <li>Kevin Tran: Business leader/Trainer</li>
      <li>Nora Hale: Writer</li>
      <li>Lucia Moreno: Business Owner</li>
      <li>Peter Caldwell: Business Owner</li>
    </ul>
    <div class="fee"><span class="label">FEE</span><span class="amount">$30</span></div>
    <p class="includes">Includes continental breakfast, lunch, and light refreshments throughout the conference.</p>
  </section>

  <footer class="web-band">WWW.BRIGHTLEDGERDAY.COM</footer>
</main>
</body>
</html>
```